Research Program Web Site

Goal:
-Create photoshop or HTML+CSS mockup of homepage for the Program for Knowledge Systems .
- Also create a child page which would be used to frame more detailed information - e.g. a list of publications, blog page, project activities, staff page.
Details:
The homepage is intended to convey:
- The mission of the program
- Link to overviews of research projects, preferably with brief teaser descriptions
- Display information on upcoming events, publications and tweets
- Show a connection to Varnholt and the Varnholt libraries
- Encourage viewers to follow/share content via social studio
Target audience:
- Research funders interested in an overview of the program, its major research areas, and research outputs (such as program publications and software, awards)
- Varnholt community (faculty, library staff, and students) interested in current information (blogs/tweets), events, and possible collaboration opportunities
Hosting:
- The site will eventually be hosted on datacraft.varnholt.example using a CMS (Drupal)
- There will be opportunity for further website implementation work if desired
Existing material:
- A text overview of the research program is included in the appendix attached to this document
- Much of the information on research projects is currently described here: http://drjbrenner.blogspot.example/dr-brenners-ongoing-studies-and-work-aka-what-is-joel-up-to/ This content will be moved to the program site when completed.
Themes:
- Varnholt color scheme is here, it is not required, but could be used for inspiration: http://web.varnholt.example/visualstyle/palette/index.html
- Varnholt libraries home page is here: http://libraries.varnholt.example/.
- The program page should borrow some design element from the library page if possible, and include the library and Varnholt logos somewhere on the page - but not as the most prominent branding element.
- Overall look and feel should be professional and serious, but modern
Comparison sites:
For comparison here are several pages for similar sites that are done fairly well:
http://www.orlandsurvey.example/
http://www.studio.varnholt.example/
http://www.dq.kestrelford.example/
- The orland and studio sites have the cleanest design.
- Both orland and dq are successful in conveying information about upcoming evevnts, publication and tweets
- Studio lab shows the right connection to larger organization
- Orland site communicates better the mission of the organization
Updates
A number of you have noted that the program description attachment was missing. I have now uploaded it. Thanks much - Joel
Thanks to those who have submitted designs so far. I have noticed that none of the designs thus far submitted include all of the elements requested in the design brief (task description). For clarification, I will emphasize these required elements:
- an area to describe the mission of the program
4. Branding/theming
Reason: Provide additional time for review of designs by colleagues on this end
Thanks,
Joel
Target Market(s)
- Research funders interested in an overview of the program, its major research areas, and research outputs (such as program publications and software
Industry/Entity Type
Library
Requirements
Nice to have
- hemes:
Comparison sites:
http://www.studio.varnholt.example/

```html
<!DOCTYPE html>
<html lang="en">
<head>
<meta charset="utf-8">
<title>Program of Knowledge Systems — Varnholt Libraries</title>
<link rel="stylesheet" href="https://fonts.googleapis.com/css2?family=Exo+2:wght@400;500;600&family=Quicksand:wght@400;500&display=swap">
<style>
:root{
  --ink:#363a4a;
  --ink-dark:#2a2c35;
  --accent:#e8283c;
  --text:#3a3a3a;
  --muted:#8a8a8a;
  --rule:#bdbdbd;
  --hero:#9c9ea6;
  --paper:#ffffff;
}
*{box-sizing:border-box;margin:0;padding:0}
html,body{width:928px;height:1200px;overflow:hidden;background:var(--paper)}
body{position:relative;font-family:"Quicksand",sans-serif;color:var(--text);font-size:10.5px;line-height:13px}
.abs{position:absolute}
h1,h2,h3,.nav,.brand{font-family:"Exo 2",sans-serif}

/* header */
.site-header{left:0;top:0;width:928px;height:61px;background:var(--ink);color:#fff}
.brand{left:122px;top:11px;font-size:14px;letter-spacing:.2px}
.brand b{font-weight:600}
.program-title{left:122px;top:29px;font-size:19px;font-weight:400;letter-spacing:.3px;font-family:"Exo 2",sans-serif}
.nav{top:12px;font-size:12px;font-weight:500}
.nav a{color:#fff;text-decoration:none;position:absolute;white-space:nowrap}
.nav a.active{color:var(--accent)}
.top-rule{left:116px;top:90px;width:696px;height:1px;background:#555}

/* left column */
.side-block{left:123px;width:218px}
.side-bar{width:218px;height:4px;background:var(--ink)}
.side-title{font-size:14.5px;font-weight:600;text-align:center;color:var(--ink-dark);padding:8px 0 7px;border-bottom:1px solid var(--rule);letter-spacing:.2px}
.about p{margin-top:10px;font-size:10.6px;line-height:13px}
.feed-item{text-align:center;margin-top:10px;font-size:10.6px;line-height:13px}
.feed-meta{color:var(--accent);font-size:8.3px;margin-top:3px}
.feed-item a{color:var(--accent);text-decoration:none}
.view-more{text-align:right;color:var(--accent);font-size:8.5px;font-style:italic;margin-top:2px}
.pub{position:absolute;left:0;width:218px}
.pub h3{font-size:13px;font-weight:500;color:var(--ink-dark)}
.pub .by{font-size:8.5px}
.pub p{width:108px;margin-top:15px;font-size:10.6px;line-height:13px}
.pub .more{position:absolute;left:52px;color:var(--accent);font-style:italic;font-size:10.5px}
.cover{position:absolute;left:116px;width:102px}

/* main */
.hero{left:355px;top:119px;width:450px;height:326px;background:var(--hero);color:#fff}
.hero-img{position:absolute;left:14px;top:14px;width:422px;height:207px;background:linear-gradient(180deg,#a8c07a 0%,#5f8a3a 45%,#e4e2dc 60%,#8a8474 100%)}
.tag{position:absolute;background:var(--accent);color:#fff;font-family:"Exo 2",sans-serif;font-weight:600;font-size:10.5px;padding:2px 6px;line-height:13px}
.hero h2{position:absolute;left:14px;top:229px;font-size:14.5px;font-weight:600;letter-spacing:.2px}
.hero p{position:absolute;left:14px;top:246px;width:416px;font-size:10.4px;line-height:13px}

.entry{position:absolute;width:218px}
.entry .img{width:218px}
.entry h2{font-size:14px;font-weight:600;color:var(--ink-dark);line-height:17px;letter-spacing:.2px}
.entry p{font-size:10.6px;line-height:13px}
.read{display:block;text-align:right;color:var(--accent);font-style:italic;font-size:10.5px}
.rule{position:absolute;height:1px;background:var(--rule);width:218px}

.pager{top:1054px;height:18px;font-family:"Exo 2",sans-serif;font-size:10px;font-weight:600}
.pager span{position:absolute;top:0;width:18px;height:18px;line-height:18px;text-align:center;background:var(--ink-dark);color:#fff}
.pager span.on{background:var(--accent)}
.pager span.next{width:39px}

/* footer */
.site-footer{left:0;top:1087px;width:928px;height:73px;background:var(--ink);color:#fff;font-size:9px}
.footer-nav{position:absolute;left:114px;top:21px;letter-spacing:.3px}
.footer-nav i{font-style:normal;margin:0 7px}
.footer-rule{position:absolute;top:35px;height:1px;background:#777}
.contact{position:absolute;top:44px;display:flex;align-items:center;gap:6px}
.stay{position:absolute;left:644px;top:21px}
.social{position:absolute;left:644px;top:44px;display:flex;gap:4px}
.social span{width:11px;height:11px;background:#d8d8de;border-radius:2px}
.notch{position:absolute;left:457px;top:0}
.base{left:0;top:1160px;width:928px;height:40px;background:var(--ink-dark);color:#fff}
.base .lib{position:absolute;left:116px;top:13px;font-family:"Exo 2",sans-serif;font-size:12px}
.base .inst{position:absolute;left:182px;top:9px;font-family:"Exo 2",sans-serif;font-size:17px;font-weight:600;padding-right:8px;border-right:1px solid #888}
.base .inst-name{position:absolute;left:229px;top:24px;font-size:7.5px;letter-spacing:1.3px;text-transform:uppercase;color:#cfd0d6}
.base .right{position:absolute;right:115px;top:12px;font-size:9.5px}
</style>
</head>
<body>

<header class="abs site-header">
  <div class="abs brand"><b>VARNHOLT</b>LIBRARIES</div>
  <div class="abs program-title">PROGRAM OF KNOWLEDGE SYSTEMS</div>
  <nav class="abs nav" style="left:0;width:928px">
    <a class="active" style="left:519px">HOME</a>
    <a style="left:570px">PUBLICATIONS</a>
    <a style="left:662px">BLOG</a>
    <a style="left:706px">PROJECTS</a>
    <a style="left:772px">STAFF</a>
  </nav>
</header>
<div class="abs top-rule"></div>

<!-- left column -->
<section class="abs side-block about" style="top:119px">
  <div class="side-bar"></div>
  <h1 class="side-title">ABOUT THE PROGRAM</h1>
  <p>Lorem ipsum dolor sit amet, consectetur adipiscing elit. Donec nec erat eu nunc pulvinar blandit in a mi. Pellentesque dui ipsum, placerat in sollicitudin quis, blandit vel leo. Aliquam tortor turpis, volutpat id facilisis et, pulvinar sit amet dolor. Nullam tempor tortor tincidunt orci laoreet sollicitudin. Morbi quis eros lacus, vel tincidunt purus. Pellentesque euismod blandit urna ullamcorper vestibulum. Curabitur consequat pellentesque libero eu molestie. Sed at ligula sit amet nunc laoreet hendrerit.</p>
</section>

<section class="abs side-block newsfeed" style="top:340px">
  <div class="side-bar"></div>
  <h1 class="side-title">NEWSFEED</h1>
  <div class="feed-item">Lorem ipsum dolor sit amet, consectetur adipiscing elit. Suspendisse imperdiet.<div class="feed-meta">1 hour ago • reply • retweet • favorite</div></div>
  <div class="feed-item">Lorem ipsum dolor sit amet, consectetur adipiscing elit. Suspendisse imperdiet. Nam posuere ipsum sit amet metus viverra.<div class="feed-meta">4 days ago • reply • retweet • favorite</div></div>
  <div class="feed-item">Lorem ipsum dolor sit amet, consectetur adipiscing elit. Suspendisse imperdiet. <a>#Varnholt</a><div class="feed-meta">4 days ago • reply • retweet • favorite</div></div>
  <div class="feed-item">Lorem ipsum dolor!<br><a>http://plan.varnholt.example/programs</a><div class="feed-meta">5 days ago • reply • retweet • favorite</div></div>
  <div class="feed-item"><a>@VarnholtNews</a> Lorem ipsum dolor sit amet, consectetur adipiscing elit. Suspendisse imperdiet.<div class="feed-meta">6 days ago • reply • retweet • favorite</div></div>
  <div class="view-more">View More »</div>
</section>

<section class="abs side-block publications" style="top:686px;height:360px">
  <div class="side-bar"></div>
  <h1 class="side-title">RECENT PUBLICATIONS</h1>
  <div class="pub" style="top:44px">
    <h3>Meshworks</h3>
    <div class="by">By: Dana Whitcombe</div>
    <p>How social networks, the personalized Internet, and always-on mobile connectivity are transforming and expanding social life.</p>
    <span class="more" style="top:146px">View More</span>
    <div class="cover" style="top:3px;height:152px;background:radial-gradient(circle at 40% 40%,#6fb6e8,#1f5aa8 55%,#14316e)" role="img" aria-label="Book cover for Meshworks: blue cover with light burst motifs"></div>
  </div>
  <div class="pub" style="top:214px">
    <h3>Free Shelves</h3>
    <div class="by">By: Tobias Ferrand</div>
    <p>The Internet lets us share perfect copies of our work with a worldwide audience at virtually no cost.</p>
    <span class="more" style="top:125px">View More</span>
    <div class="cover" style="top:3px;height:145px;background:linear-gradient(180deg,#111 0%,#111 90%,#f26b0f 90%)" role="img" aria-label="Book cover for Free Shelves: black cover with orange band"></div>
  </div>
</section>

<!-- hero -->
<section class="abs hero">
  <div class="hero-img" role="img" aria-label="Photo of a passenger train passing through green hills"></div>
  <span class="tag" style="left:14px;top:208px">Technology</span>
  <h2>HEADER AND IMAGE SCREEN</h2>
  <p>You can have your most prominent or up-and-coming projects on display here. Images can be used to enhance viewer sensation. Time for more lorem ipsum! Lorem ipsum dolor sit amet, consectetur adipiscing elit. Donec nec erat eu nunc pulvinar blandit in a mi. Pellentesque dui ipsum, placerat in sollicitudin quis, blandit vel leo. Oups made some spelling mistakes.</p>
</section>

<!-- column one -->
<article class="entry" style="left:355px;top:471px">
  <div class="img" style="height:144px;background:linear-gradient(135deg,#1d3f8f,#0f2560 60%,#1a1a22)" role="img" aria-label="Photo of a speaker waving on a blue stage"></div>
  <span class="tag" style="left:0;top:127px">Politics</span>
  <h2 style="margin-top:9px">IMAGE, HEADER, WITH TAG AND TEASER TEXT</h2>
  <p>Quisque iaculis orci in ligula malesuada tempor. Fusce ullamcorper laoreet varius. Pellentesque lobortis mollis elit, tristique adipiscing purus dignissim et.</p>
  <span class="read" style="margin-top:4px">Read more »</span>
</article>
<div class="rule" style="left:355px;top:733px"></div>
<article class="entry" style="left:355px;top:742px">
  <h2>HEADER AND TEXT ONLY ENTRY</h2>
  <p>Quisque iaculis orci in ligula malesuada tempor. Fusce ullamcorper laoreet varius. Pellentesque lobortis mollis elit, tristique adipiscing purus dignissim et.</p>
  <span class="read" style="margin-top:4px">Read more »</span>
</article>
<article class="entry" style="left:355px;top:846px">
  <div class="img" style="height:144px;background:linear-gradient(160deg,#8a8a8a,#3a3a3e 55%,#1c1c20)" role="img" aria-label="Photo of traders on a busy exchange floor"></div>
  <span class="tag" style="left:0;top:127px">Business</span>
  <h2 style="margin-top:12px">IMAGE, HEADER ONLY ENTRY</h2>
  <span class="read">Read more »</span>
</article>
<div class="rule" style="left:355px;top:1041px"></div>

<!-- column two -->
<div class="rule" style="left:587px;top:460px"></div>
<article class="entry" style="left:587px;top:469px">
  <h2>HEADER AND TEXT ONLY ENTRY</h2>
  <p>Quisque iaculis orci in ligula malesuada tempor. Fusce ullamcorper laoreet varius. Pellentesque lobortis mollis elit, tristique adipiscing purus dignissim et.</p>
  <span class="read" style="margin-top:4px">Read more »</span>
</article>
<article class="entry" style="left:587px;top:572px">
  <div class="img" style="height:144px;background:linear-gradient(180deg,#c7c9bd,#6f7368 50%,#2a2c2a)" role="img" aria-label="Photo of officials reviewing an honour guard"></div>
  <span class="tag" style="left:0;top:127px">Business</span>
  <h2 style="margin-top:7px">IMAGE, HEADER ONLY ENTRY</h2>
  <span class="read">Read more »</span>
</article>
<div class="rule" style="left:587px;top:767px"></div>
<article class="entry" style="left:587px;top:776px">
  <div class="img" style="height:145px;background:linear-gradient(180deg,#2f8fd8,#1d5e9e 55%,#5d7a70)" role="img" aria-label="Photo of a sea turtle swimming over a reef"></div>
  <span class="tag" style="left:0;top:128px">Science</span>
  <h2 style="margin-top:9px">IMAGE, HEADER, WITH TAG AND TEASER TEXT</h2>
  <p>Quisque iaculis orci in ligula malesuada tempor. Fusce ullamcorper laoreet varius. Pellentesque lobortis mollis elit, tristique adipiscing purus dignissim et.</p>
  <span class="read" style="margin-top:4px">Read more »</span>
</article>
<div class="rule" style="left:587px;top:1041px"></div>

<div class="abs pager" style="left:0;width:928px">
  <span class="on" style="left:632px">1</span>
  <span style="left:658px">2</span>
  <span style="left:684px">3</span>
  <span style="left:710px">4</span>
  <span style="left:736px">5</span>
  <span class="next" style="left:764px">next »</span>
</div>

<!-- footer -->
<footer class="abs site-footer">
  <svg class="notch" width="14" height="7" viewBox="0 0 14 7"><path d="M0 0H14L7 7Z" fill="#fff"/></svg>
  <div class="footer-nav">HOME<i>|</i>PUBLICATIONS<i>|</i>BLOG<i>|</i>PROJECTS<i>|</i>STAFF</div>
  <div class="footer-rule" style="left:114px;width:518px"></div>
  <div class="contact" style="left:115px">
    <svg width="12" height="11" viewBox="0 0 12 11"><path d="M6 0L0 5H2V11H5V7H7V11H10V5H12Z" fill="#fff"/></svg>
    <span>412 Harlow Street | Eastbury, MA</span>
  </div>
  <div class="contact" style="left:326px">
    <svg width="11" height="8" viewBox="0 0 11 8"><rect width="11" height="8" fill="#fff"/><path d="M0 0L5.5 4.5L11 0" stroke="#363a4a" fill="none"/></svg>
    <span>contact@varnholt-pks.example</span>
  </div>
  <div class="contact" style="left:477px">
    <svg width="11" height="11" viewBox="0 0 11 11"><path d="M2 0L4 3L3 4.5C4 6.5 5 7.5 6.5 8L8 7L11 9L9.5 11C4.5 10.5 0.5 6.5 0 1.5Z" fill="#fff"/></svg>
    <span>555.014.2300</span>
  </div>
  <div class="stay">STAY CONNECTED</div>
  <div class="footer-rule" style="left:644px;width:167px"></div>
  <div class="social"><span></span><span></span><span></span><span></span><span></span></div>
</footer>
<div class="abs base">
  <div class="lib">Varnholt Libraries</div>
  <div class="inst" style="left:232px;top:6px;font-size:13px;border:none">Varnholt</div>
  <div class="inst-name">Varnholt Institute of Technology</div>
  <div class="right"><b>Varnholt</b>Libraries | Program of Knowledge Systems</div>
</div>

</body>
</html>
```